Real Estate Company Needs a Contemporary/Modern Business Card Design

We need a Contemporary/Modern Business Card Design for a New Real Estate Company based in San Francisco, CA called Tolvash Orrin Realtors. We would like to see designs that use the color red for the "Tolvash Orrin" and gold for the "Realtors." The design should communicate being Modern and yet Established and Stable.
Updates

Project Deadline Extended
Reason: Waiting for more designs and/or revisions.

Industry/Entity Type

Business

```html
<!DOCTYPE html>
<html lang="en">
<head>
<meta charset="utf-8">
<title>Tolvash Orrin Realtors – Business Card</title>
<link rel="stylesheet" href="https://fonts.googleapis.com/css2?family=Montserrat:wght@700&family=Open+Sans:wght@700&display=swap">
<style>
  :root {
    --brand-red: #990000;
    --brand-gold: #7a6b2d;
    --paper: #ffffff;
    --page: #fdfdfd;
    --card-edge: #b9b9b9;
    --text-light: #ffffff;
  }
  * { margin: 0; padding: 0; box-sizing: border-box; }
  html, body {
    width: 1200px;
    height: 849px;
    overflow: hidden;
    background: var(--page);
  }
  .canvas {
    position: relative;
    width: 1200px;
    height: 849px;
  }
  .card {
    position: absolute;
    top: 304px;
    width: 458px;
    height: 242px;
  }
  .card--front {
    left: 121px;
    background: var(--brand-red);
  }
  .card--back {
    left: 623px;
    background: var(--paper);
    border: 1px solid var(--card-edge);
  }

  /* Front */
  .front-ring {
    position: absolute;
    left: 211px;
    top: 63px;
    width: 36px;
    height: 36px;
    border: 3px solid var(--text-light);
    border-radius: 50%;
  }
  .company-name {
    position: absolute;
    left: 0;
    right: 0;
    top: 116px;
    text-align: center;
    font-family: "Montserrat", sans-serif;
    font-weight: 700;
    font-size: 15px;
    letter-spacing: 4.2px;
    color: var(--text-light);
    text-transform: uppercase;
    padding-left: 4px;
  }
  .name-rule {
    position: absolute;
    left: 210px;
    top: 141px;
    width: 38px;
    height: 1px;
    background: var(--brand-gold);
  }
  .company-type {
    position: absolute;
    left: 0;
    right: 0;
    top: 147px;
    text-align: center;
    font-family: "Montserrat", sans-serif;
    font-weight: 700;
    font-size: 12.5px;
    letter-spacing: 2.4px;
    color: var(--brand-gold);
    text-transform: uppercase;
    padding-left: 2px;
  }

  /* Back */
  .back-mark {
    position: absolute;
    left: 0;
    right: 0;
    top: 76px;
    display: flex;
    justify-content: center;
    align-items: center;
    gap: 12px;
  }
  .back-ring {
    width: 60px;
    height: 60px;
    border: 5px solid var(--brand-red);
    border-radius: 50%;
  }
  .back-name {
    font-family: "Montserrat", sans-serif;
    font-weight: 700;
    font-size: 15px;
    letter-spacing: 2px;
    color: var(--brand-red);
    text-transform: uppercase;
  }
  .agent-name {
    position: absolute;
    left: 24px;
    top: 151px;
    font-family: "Montserrat", sans-serif;
    font-weight: 700;
    font-size: 13px;
    letter-spacing: 1.2px;
    color: var(--brand-gold);
    text-transform: uppercase;
  }
  .contact-list {
    position: absolute;
    left: 24px;
    top: 175px;
    list-style: none;
    font-family: "Open Sans", sans-serif;
    font-weight: 700;
    font-size: 11.5px;
    line-height: 15px;
    color: var(--brand-red);
  }
</style>
</head>
<body>
  <main class="canvas">
    <section class="card card--front" aria-label="Card front">
      <div class="front-ring"></div>
      <h1 class="company-name">Tolvash Orrin</h1>
      <div class="name-rule"></div>
      <p class="company-type">Realtors</p>
    </section>

    <section class="card card--back" aria-label="Card back">
      <div class="back-mark">
        <div class="back-ring"></div>
        <span class="back-name">Tolvash Orrin</span>
      </div>
      <h2 class="agent-name">Dara Venn</h2>
      <ul class="contact-list">
        <li class="contact-phone">5550 2817</li>
        <li class="contact-email">dvenn@mailbox.test</li>
        <li class="contact-address">Address goes here</li>
      </ul>
    </section>
  </main>
</body>
</html>
```